Crowdsourced IT recruitment agency - brivon

We need an engaging and smart website design for BRIVON Crowd recruitment. We are young innovative IT recruitment company. We have deep expertise in all IT & digital areas and using crowdsourcing to search the best market candidates faster than ever.
Our mission: to connect people and organizations interests, inspiring each other and enabling together reach better results.

We would like the design to be personalized, emotional, yet simple and neat. It should focus on the person with a problem which we solve.

Reading the site customers should feel safe and confident that brivon is the trusted partner and everything we do is a quality product.

We also focus on long term relationship with our clients.

We have 4 products:
IT Recruitment – professional recruitment of candidates in IT and digital areas
IT RPO – candidates research process outsourcing(RPO) - provision of resume pools for the client
Velmar Academy – training, seminars and networking events for HR professionals from IT and hi-tech companies
HR Dashboard – a tool for data visualization in nice and interactive dashboards. It pulls data from different corporate sources (SAP, Oracle, excel, etc.). It looks like a dashboard, on which there are several graphs or diagrams with HR and business KPIs(key performance indicators)

We like material design sites but also open for other options/ideas

Current site brivon.ru

Examples of websites that we like:
http://www.kelmo.ru
https://pinegroverun.ru

Site structure:
About us (description, mission, team, clients, office)
Products: HR Dashboard, HR IPO, It Recruitment
Velmar Academy (list of events (past and future) with the ability to upload photos, descriptions, etc.)
News: Publications, Articles, Blog
Contacts

Industry/Entity Type

Consulting

Number of Pages Required

5+ page

Font styles to use
Serif
Sans Serif

Requirements
Must have
• Individual blocks with the transition to a separate page for each product
• Link to social network (fb, link),
• Subscribe to news on the main page
• Feedback form
• Site structure:
• About us (description, mission, team, clients, office)
• Products: HR Dashboard, HR IPO, It Recruitment
• Velmar Academy (list of events (past and future) with the ability to upload photos, descriptions, etc.)
• News: Publications, Articles, Blog, Calendars
• Contacts
Should not have
• too crowded
• too complicatied
• without advertising banners
• crammed

```html
<!DOCTYPE html>
<html lang="en">
<head>
<meta charset="utf-8">
<title>Brivon — Get in Touch</title>
<link href="https://fonts.googleapis.com/css2?family=Bebas+Neue&family=Open+Sans:wght@400;700&display=swap" rel="stylesheet">
<style>
  :root {
    --sidebar: #231f20;
    --page: #1b5790;
    --logo: #0f4a86;
    --field: #f4f4f4;
    --placeholder: #b9b9b9;
    --white: #ffffff;
    --accent: #2a9fd8;
  }
  * { margin: 0; padding: 0; box-sizing: border-box; }
  html, body { width: 1200px; height: 800px; overflow: hidden; }
  body {
    position: relative;
    background: var(--page);
    font-family: "Open Sans", Arial, sans-serif;
    color: var(--white);
  }
  .sidebar {
    position: absolute; left: 0; top: 0;
    width: 100px; height: 800px;
    background: var(--sidebar);
  }
  .sidebar svg { position: absolute; display: block; }
  .menu-icon { left: 32px; top: 38px; }
  .share-icon { left: 32px; top: 132px; }
  .news-icon { left: 32px; top: 222px; }
  .mail-icon { left: 28px; top: 323px; }

  .brand {
    position: absolute; left: 182px; top: 18px;
    display: flex; align-items: center; gap: 14px;
    color: var(--logo);
    font-weight: 700; font-size: 26px;
  }
  .brand-dot {
    width: 62px; height: 62px; border-radius: 50%;
    background: var(--logo);
  }

  .contact-title {
    position: absolute; left: 188px; top: 322px;
    font-family: "Bebas Neue", Impact, sans-serif;
    font-size: 50px; line-height: 1; font-weight: 400;
    letter-spacing: -0.5px;
  }
  .contact-form .field {
    position: absolute; left: 188px; width: 524px; height: 64px;
    background: var(--field);
    border: none; outline: none;
    padding: 0 28px;
    font-family: inherit; font-size: 19px; color: #444;
  }
  .contact-form .field::placeholder { color: var(--placeholder); }
  .field-name { top: 400px; }
  .field-email { top: 480px; }
  .field-subject { top: 560px; }
  .field-message { top: 640px; height: 96px !important; padding-top: 18px !important; resize: none; }

  .contact-info { position: absolute; left: 770px; top: 506px; width: 400px; }
  .contact-info h2 { font-size: 19px; font-weight: 700; margin-left: 1px; }
  .contact-info address {
    font-style: normal; font-size: 14.5px; line-height: 18px;
    margin-top: 22px;
  }
  .contact-line { font-size: 14.5px; margin-top: 16px; }
  .contact-line .divider { margin: 0 20px; }

  .submit-button {
    position: absolute; left: 771px; top: 672px;
    width: 81px; height: 64px; border: none;
    background: var(--field);
    display: flex; align-items: center; justify-content: center;
  }
</style>
</head>
<body>
  <nav class="sidebar">
    <svg class="menu-icon" width="36" height="20" viewBox="0 0 36 20">
      <g stroke="#fff" stroke-width="2"><line x1="0" y1="2" x2="36" y2="2"/><line x1="0" y1="9" x2="36" y2="9"/><line x1="0" y1="16" x2="36" y2="16"/></g>
    </svg>
    <svg class="share-icon" width="36" height="38" viewBox="0 0 36 38">
      <g fill="none" stroke="#fff" stroke-width="1.8">
        <line x1="6" y1="19" x2="29" y2="6"/><line x1="6" y1="19" x2="29" y2="32"/>
        <circle cx="29" cy="6" r="4" fill="var(--sidebar)"/><circle cx="6" cy="19" r="4" fill="var(--sidebar)"/><circle cx="29" cy="32" r="4" fill="var(--sidebar)"/>
      </g>
    </svg>
    <svg class="news-icon" width="40" height="38" viewBox="0 0 40 38">
      <g fill="none" stroke="#fff" stroke-width="1.6">
        <rect x="1" y="1" width="27" height="36" rx="1"/>
        <path d="M28 7h9a2 2 0 0 1 2 2v26a2 2 0 0 1-2 2H28"/><line x1="33" y1="8" x2="33" y2="34"/>
        <line x1="5" y1="7" x2="24" y2="7"/><line x1="5" y1="12" x2="24" y2="12"/>
        <line x1="5" y1="17" x2="12" y2="17"/><line x1="5" y1="21" x2="12" y2="21"/><line x1="5" y1="25" x2="12" y2="25"/><line x1="5" y1="29" x2="12" y2="29"/>
        <line x1="16" y1="17" x2="24" y2="17"/><line x1="16" y1="21" x2="24" y2="21"/><line x1="16" y1="25" x2="24" y2="25"/><line x1="16" y1="29" x2="24" y2="29"/>
      </g>
    </svg>
    <svg class="mail-icon" width="50" height="40" viewBox="0 0 50 40">
      <g fill="none" stroke="var(--accent)" stroke-width="1.6">
        <path d="M10 1h37a1.5 1.5 0 0 1 1.5 1.5V28a1.5 1.5 0 0 1-1.5 1.5h-5"/>
        <rect x="1" y="8" width="40" height="28" rx="1.5"/>
        <path d="M1 9l20 16 20-16"/><path d="M1 36l14-12M41 36L27 24"/>
        <line x1="13" y1="39" x2="29" y2="39"/>
      </g>
      <path d="M12 11h18l-9 7z" fill="var(--accent)"/>
    </svg>
  </nav>

  <div class="brand"><span class="brand-dot"></span><span>brivon</span></div>

  <h1 class="contact-title">Get in touch</h1>

  <form class="contact-form">
    <input class="field field-name" type="text" placeholder="Your Name">
    <input class="field field-email" type="email" placeholder="Email">
    <input class="field field-subject" type="text" placeholder="Subject">
    <textarea class="field field-message" placeholder="Message"></textarea>
  </form>

  <section class="contact-info">
    <h2>Contact Info</h2>
    <address>Lindenweg ul. 42, Marsk village, Olvensky District,<br>Tverdan Region, 190455, Russia</address>
    <p class="contact-line">+7 (000) 555 0 182<span class="divider">|</span>info@brivon.ru</p>
  </section>

  <button class="submit-button" type="submit" aria-label="Send">
    <svg width="28" height="16" viewBox="0 0 28 16"><g fill="none" stroke="var(--accent)" stroke-width="1.6"><line x1="1" y1="8" x2="26" y2="8"/><path d="M19 1l7 7-7 7"/></g></svg>
  </button>
</body>
</html>
```